Purchase Protection Subscription Program needs a refreshed website

We are refreshing an existing website www.buyguardian720.com. This is a purchase protection product which allows its members to receive extended warranty on the items they buy, receive a rebate of 50% on a repair of an item, a personal shopping concierge, etc. We are looking for a fresh, clean approach - with mass appeal to both men and woman. The site should convey trust, and ease of use.
Updates

Thanks to everyone who posted designs. Amazing work! It was a very difficult decision!

Industry/Entity Type

Product

```html
<!DOCTYPE html>
<html lang="en">
<head>
<meta charset="utf-8">
<title>BuyGuardian 720 — Shop with Confidence</title>
<link href="https://fonts.googleapis.com/css2?family=Titillium+Web:wght@300;400;600;700&display=swap" rel="stylesheet">
<style>
:root{
  --header-bg:#e8ecef;
  --ink:#3a3a3a;
  --ink-soft:#777;
  --ink-muted:#9a9a9a;
  --red:#c9252b;
  --red-dark:#a81c21;
  --orange:#f07a1e;
  --panel:#f5f5f5;
  --rule:#dedede;
  --link-blue:#2a9fd6;
  --footer-bg:#f3f3f3;
  --bar-bg:#1e1e1e;
  --white:#fff;
}
*{box-sizing:border-box;margin:0;padding:0}
html,body{width:1024px;height:1200px;overflow:hidden}
body{position:relative;font-family:"Titillium Web",sans-serif;color:var(--ink);background:var(--white)}
.abs{position:absolute}
a{color:inherit;text-decoration:none}

.site-header{left:0;top:0;width:1024px;height:74px;background:var(--header-bg)}
.brand{font-family:"Titillium Web",sans-serif;font-weight:400;color:#1e1e1e;font-size:21px;letter-spacing:-.2px;white-space:nowrap}
.header-brand{left:142px;top:13px}
.utility-links{left:492px;top:20px;display:flex;font-size:12px;color:var(--ink-soft)}
.utility-links a{padding:0 16px;border-left:1px solid #c9cdd0;line-height:16px}
.utility-links a:first-child{border-left:0}
.btn{display:flex;align-items:center;justify-content:center;font-weight:600;border-radius:2px}
.btn-login{left:706px;top:12px;width:88px;height:31px;background:linear-gradient(#fff,#eceef0);border:1px solid #c5c9cc;color:#666;font-size:11px}
.btn-register{left:800px;top:12px;width:88px;height:31px;background:var(--red);border:1px solid var(--red-dark);color:#fff;font-size:11px}

.main-nav{left:136px;top:54px;width:752px;height:40px;background:linear-gradient(#fff,#f4f4f4);border:1px solid #d6d6d6;border-radius:2px;z-index:2}
.main-nav a{position:absolute;top:12px;font-size:11.5px;font-weight:600;color:#777}

.hero{left:0;top:74px;width:1024px;height:368px;background:linear-gradient(90deg,#b6a46a 0%,#7a8f5a 18%,#3f7fa6 36%,#c4d3dc 52%,#eef2f5 68%,#dfe6ec 100%)}
.hero-title{left:542px;top:190px;font-size:34px;font-weight:700;color:#333;white-space:nowrap}
.hero-sub{left:542px;top:236px;font-size:19px;font-weight:400;color:#777;white-space:nowrap}
.btn-hero{left:542px;top:293px;width:112px;height:36px;background:var(--red);color:#fff;font-size:13px;border-radius:2px}

.features{left:0;top:442px;width:1024px;height:438px;background:var(--panel)}
.portrait{width:172px;height:172px;border-radius:50%;top:478px}
.portrait-a{left:170px;background:radial-gradient(circle at 50% 45%,#8a8a8a 0,#bdbdbd 30%,#ffffff 62%)}
.portrait-b{left:428px;background:radial-gradient(circle at 50% 50%,#6f6f6f 0,#a7a7a7 28%,#ffffff 62%)}
.portrait-c{left:683px;background:radial-gradient(circle at 50% 55%,#4f5a8a 0,#3aa0a0 24%,#e9ecef 55%,#ffffff 66%)}
.divider{width:1px;top:670px;height:160px;background:var(--rule)}
.feature{top:674px}
.feature h2{display:flex;align-items:center;gap:8px;font-size:13px;font-weight:600;color:#333;white-space:nowrap}
.feature h2 svg{flex:none}
.feature p{font-size:9.8px;line-height:14.4px;color:var(--ink-muted)}
.feature .lead{margin-top:17px;font-weight:600;color:#8a8a8a}
.checks{display:grid;grid-template-columns:146px 100px;font-size:9.8px;line-height:19.2px;color:var(--ink-muted);margin-top:1px;list-style:none}
.checks li{display:flex;gap:5px;align-items:center}
.checks li.cont{padding-left:14px}
.checks svg{flex:none}
.accent{color:var(--red);font-weight:600}
.btn-more{top:798px;width:88px;height:32px;background:linear-gradient(#fff,#f0f0f0);border:1px solid #c8c8c8;color:#777;font-size:11px;font-weight:400;border-radius:2px;box-shadow:0 1px 1px rgba(0,0,0,.08)}

.cta-band{left:0;top:880px;width:1024px;height:67px;background:var(--red)}
.cta-text{left:226px;top:893px;font-size:29px;font-weight:400;color:#fff;white-space:nowrap}
.btn-cta{left:708px;top:898px;width:110px;height:34px;background:var(--orange);border:1px solid #d96412;color:#fff;font-size:12px;border-radius:2px}

.site-footer{left:0;top:947px;width:1024px;height:222px;background:repeating-linear-gradient(135deg,#f6f6f6 0 2px,#efefef 2px 4px)}
.footer-brand{left:134px;top:972px}
.footer-col{top:975px;font-size:11px;color:#999}
.footer-col h3{font-size:11.5px;font-weight:400;color:#444;margin-bottom:7px}
.footer-col li{list-style:none;line-height:24px}
.footer-col li.current{color:var(--link-blue)}
.contact-line{display:flex;align-items:center;gap:9px;font-size:9.5px;color:#6a7fa0;line-height:22px}
.social{display:flex;gap:12px;margin-top:7px}
.social span{width:26px;height:26px;display:block}
.social .s1{background:#3b5a98}
.social .s2{background:#2aa3dc}
.social .s3{background:#1b6ea8}
.disclaimer{left:127px;top:1090px;width:780px;font-size:8.7px;line-height:14.4px;color:#a3a3a3}

.bottom-bar{left:0;top:1169px;width:1024px;height:31px;background:var(--bar-bg);font-size:9.5px;color:#bbb}
.bottom-bar .copy{position:absolute;left:142px;top:9px}
.bottom-bar .legal{position:absolute;top:9px}
</style>
</head>
<body>

<header class="site-header abs"></header>
<div class="brand header-brand abs">BuyGuardian 720</div>
<nav class="utility-links abs"><a href="#">Manage</a><a href="#">User</a><a href="#">Profile</a></nav>
<a class="btn btn-login abs" href="#">Login</a>
<a class="btn btn-register abs" href="#">Register</a>

<nav class="main-nav abs">
  <a href="#" style="left:29px">Home</a>
  <a href="#" style="left:101px">About</a>
  <a href="#" style="left:174px">Product Features</a>
  <a href="#" style="left:302px">How It Works</a>
  <a href="#" style="left:412px">Privacy</a>
  <a href="#" style="left:492px">Contact Us</a>
</nav>

<section class="hero abs" role="img" aria-label="Photo of a smiling young couple carrying shopping bags in a bright shopping mall"></section>
<h1 class="hero-title abs">Shop with Confidence</h1>
<p class="hero-sub abs">knowing BuyGuardian 720 is there.</p>
<a class="btn btn-hero abs" href="#">Get Started</a>

<section class="features abs"></section>
<div class="portrait portrait-a abs" role="img" aria-label="Round photo of a young woman holding a credit card and shopping bags"></div>
<div class="portrait portrait-b abs" role="img" aria-label="Round photo of a young man carrying shopping bags over his shoulder"></div>
<div class="portrait portrait-c abs" role="img" aria-label="Round photo of a happy young couple giving thumbs up"></div>

<div class="divider abs" style="left:385px"></div>
<div class="divider abs" style="left:641px"></div>

<article class="feature abs" style="left:138px;width:240px">
  <h2><svg width="17" height="20" viewBox="0 0 17 20"><path d="M4 9V6a4.5 4.5 0 0 1 9 0v3" fill="none" stroke="#c9252b" stroke-width="2.4"/><rect x="0" y="9" width="17" height="11" rx="1" fill="#c9252b"/><rect x="7.5" y="12" width="2" height="5" fill="#fff"/></svg>Valuable Purchase Protection</h2>
  <p class="lead">Get 5 unique ways to get more out of things you buy:*</p>
  <ul class="checks">
    <li><svg width="10" height="8" viewBox="0 0 10 8"><path d="M1 4l3 3 5-6" fill="none" stroke="#c9252b" stroke-width="2"/></svg>Warranty extension</li>
    <li><svg width="10" height="8" viewBox="0 0 10 8"><path d="M1 4l3 3 5-6" fill="none" stroke="#c9252b" stroke-width="2"/></svg>Price protection</li>
    <li><svg width="10" height="8" viewBox="0 0 10 8"><path d="M1 4l3 3 5-6" fill="none" stroke="#c9252b" stroke-width="2"/></svg>Repair bill rebate</li>
    <li><svg width="10" height="8" viewBox="0 0 10 8"><path d="M1 4l3 3 5-6" fill="none" stroke="#c9252b" stroke-width="2"/></svg>Restocking fee</li>
    <li><svg width="10" height="8" viewBox="0 0 10 8"><path d="M1 4l3 3 5-6" fill="none" stroke="#c9252b" stroke-width="2"/></svg>Product return guarantee</li>
    <li class="cont">reimbursement</li>
  </ul>
</article>
<a class="btn btn-more abs" href="#" style="left:138px">Learn More</a>

<article class="feature abs" style="left:418px;width:200px">
  <h2><svg width="20" height="19" viewBox="0 0 20 19"><path d="M6 6V4a4 4 0 0 1 8 0v2" fill="none" stroke="#c9252b" stroke-width="2"/><path d="M1 6h18l-1 13H2z" fill="#c9252b"/></svg>Easy Claims Process</h2>
  <p style="margin-top:17px">Using BuyGuardian 720 has never been easier. Just send us copies, scans or photos of your receipts — we’ll store them securely online. Then download what you need and submit your claim online.</p>
</article>
<a class="btn btn-more abs" href="#" style="left:418px">Learn More</a>

<article class="feature abs" style="left:672px;width:220px">
  <h2><svg width="17" height="20" viewBox="0 0 17 20"><path d="M4 9V6a4.5 4.5 0 0 1 9 0v3" fill="none" stroke="#c9252b" stroke-width="2.4"/><rect x="0" y="9" width="17" height="11" rx="1" fill="#c9252b"/><rect x="7.5" y="12" width="2" height="5" fill="#fff"/></svg>One Low Monthly Fee</h2>
  <p style="margin-top:16px;color:#8b9bb3">PLUS get a <span class="accent">$5 bonus rebate</span> each calendar quarter to use on home electronics and appliance purchases!*</p>
</article>
<a class="btn btn-more abs" href="#" style="left:672px">Learn More</a>

<section class="cta-band abs"></section>
<p class="cta-text abs">Start using BuyGuardian 720 today!</p>
<a class="btn btn-cta abs" href="#">Get Started Now</a>

<footer class="site-footer abs"></footer>
<div class="brand footer-brand abs">BuyGuardian 720</div>
<div class="footer-col abs" style="left:400px">
  <h3>Navigation</h3>
  <ul><li class="current">Home</li><li>About Us</li><li>Contact Us</li></ul>
</div>
<div class="footer-col abs" style="left:511px">
  <h3>Imporant Links</h3>
  <ul><li>Privacy</li><li>Product Features</li><li>How It Works</li></ul>
</div>
<div class="footer-col abs" style="left:638px">
  <h3>Contact</h3>
  <div class="contact-line"><svg width="11" height="11" viewBox="0 0 11 11"><path d="M2 0l2 2.5-1.2 1.5a7 7 0 0 0 4.2 4.2L8.5 7 11 9l-1.5 2C4.5 11 0 6.5 0 1.5z" fill="#222"/></svg>+1800 555 010 720</div>
  <div class="contact-line"><svg width="12" height="9" viewBox="0 0 12 9"><rect width="12" height="9" fill="#222"/><path d="M0 0l6 5 6-5" fill="none" stroke="#f3f3f3" stroke-width="1.2"/></svg>info@buyguardian.com</div>
</div>
<div class="footer-col abs" style="left:784px">
  <h3>Follow Us</h3>
  <div class="social"><span class="s1"></span><span class="s2"></span><span class="s3"></span></div>
</div>

<p class="disclaimer abs">*Exclusions and limitations apply. See Terms and Conditions for complete product benefit details. Warranty Extension and Repair Bill Rebate benefits are not available in Maine. Warranty Extension and Repair Bill Rebate benefits are provided by Northline Product Care Company, except in Arizona, Florida, Oklahoma and Wisconsin, where they are provided by Service Keeper, Incorporated (FL License Number 00000), both of which are located at 410 West Harbor Ave., Springfield, IL 62701, (217) 555-0140. The programs are administered by Meridian Program Solutions, Inc., 410 West Harbor Ave., Springfield, IL 62701, (217) 555-0140. Bonus Rebates are limited to one rebate per purchased item and one purchase per calendar quarter.</p>

<div class="bottom-bar abs">
  <span class="copy">Copyright © 2014 - BuyGuardian720. All rights reserved.</span>
  <a class="legal" href="#" style="left:782px">Privacy Policy</a>
  <a class="legal" href="#" style="left:862px">Sitemap</a>
</div>

</body>
</html>
```